Visitenkarten-Design für Ferienhausvermietung
Zielgruppe
Vermietung eines Ferienhauses
Aufgabenstellung
Die Visitenkarte sollte edel und hochwertig wirken...
Es wäre mir wichtig, dass die Visitenkarte im Querformat erstellt wird.
Die Farben vom Logo lauten:
green: C = 43 M = 0 Y = 100 N = 16
brown: C = 39 M = 57 J = 87 N = 53
sky blue: C = 14 M = 6 J = 6 N = 0
Aber bitte nicht so viel in den Visitenkarten verwenden. Die Visitenkarten sollen eher neutral gehalten werden.
Die Schriften
font
Lindeneck : Satisfaction
Ferienhaus : Corbert Regular
Flyer-Design für Ferienhausvermietung Flyer-Design für Ferienhausvermietung"
Es soll ein Flyer im Format DIN A4 erstellt werden. Der beidseitig bedruckt wird und dann 6seitig gefaltet wird. Ich benötige für den Flyer: Beschreibung/Ausstattung des Ferienhauses Beschreibung der Lage Beschreibung der Umgebung Anfahrt/Lage/Kontakt
Logo-Design für Ferienhaus ´Sa Morta´auf Mallorca mit eigenem Tennisplatz und Pool Logo-Design für Ferienhaus ´Sa Morta´auf Mallorca mit eigenem Tennisplatz und Pool"
Sie können sich meine Finca auf der Website: Casitorvent anschauen. Ort: Costitx Name des Hauses: Finca Reblat (heißt nur auf der Website so). Der Name am Tor Haus: Finca Sa Morta. Ich mag es gerne klassisch
Logo-Design für ein Feriendorf an der Ostsee Logo-Design für ein Feriendorf an der Ostsee"
* Nicht zu bunt, nicht zu verspielt, möglichst klar und aufgeräumt * In 2D, keine Schattierungen, keine Fotos im Hintergrund o. ä.. * Das Logo muss in allen Medien gut darstellbar sein! * Es sollte modern wirken, dennoch fröhlich, warm und einladend * Der Strand-/Wasserbezug muss deutlich we..
Flyer-Design für Ferienhaus Flyer-Design für Ferienhaus"
Flyerdesign für Ferienhaus: Din-Lang 2x gefalzt (übliche Format), 3 Seiten vorne und hinten.  Es sollte nach Möglichkeit an unsere Webseite (www.ferienhaus-kormoran-tidewik.de) angepasst werden, druckfertig sein und per PDF auf unserer Webseite zum Downloaden integriert werden können. Meh..
Logo-Design für Ferienhaus Logo-Design für Ferienhaus"
Wir suchen ein Moderenes Design gern berücksichtig in Kombination mit dem Naturpark Velmtaler Höhen. Da das Ferienhaus sich dort befindet.

```html
<!DOCTYPE html>
<html lang="de">
<head>
<meta charset="utf-8">
<title>Lindeneck Ferienhaus – Visitenkarte</title>
<link rel="stylesheet" href="https://fonts.googleapis.com/css2?family=Signika:wght@300;400&display=swap">
<style>
  :root {
    --backdrop: #2b2f33;
    --paper: #fbfcfc;
    --sky: #dde6e6;
    --brown: #3b2621;
    --ink: #2f2522;
  }
  html, body {
    margin: 0;
    width: 1200px;
    height: 900px;
    overflow: hidden;
    background: var(--backdrop);
    font-family: "Signika", sans-serif;
  }
  .card {
    position: absolute;
    left: 280px;
    width: 640px;
    height: 360px;
    background: var(--paper);
    overflow: hidden;
  }
  .card--front { top: 70px; }
  .card--back { top: 470px; }

  .wordmark {
    position: absolute;
    left: 0; right: 0;
    top: 48px;
    text-align: center;
    font-size: 42px;
    font-weight: 400;
    color: var(--brown);
    margin: 0;
    letter-spacing: 0.5px;
  }
  .brand-dot {
    position: absolute;
    left: 250px;
    top: 132px;
    width: 140px;
    height: 140px;
  }
  .web {
    position: absolute;
    left: 0; right: 0;
    top: 266px;
    text-align: center;
    font-size: 16px;
    font-weight: 400;
    color: var(--ink);
  }
  .contact-band {
    position: absolute;
    left: 0; right: 0;
    bottom: 0;
    height: 74px;
    background: var(--sky);
    color: var(--ink);
    font-size: 15px;
    font-weight: 400;
  }
  .contact-line {
    position: absolute;
    left: 0; right: 0;
    display: flex;
    justify-content: center;
    align-items: center;
    gap: 8px;
  }
  .contact-line--address { top: 17px; }
  .contact-line--reach { top: 42px; }
  .contact-line .gap { width: 8px; }
  .icon { width: 12px; height: 12px; fill: var(--ink); }

  .flap {
    position: absolute;
    inset: 0;
  }
  .seal {
    position: absolute;
    left: 192px;
    top: 54px;
    width: 256px;
    height: 256px;
  }
  .seal-name {
    position: absolute;
    left: 192px;
    top: 160px;
    width: 256px;
    text-align: center;
    font-size: 40px;
    font-weight: 400;
    color: var(--brown);
    margin: 0;
  }
</style>
</head>
<body>
  <section class="card card--front" aria-label="Visitenkarte Vorderseite">
    <p class="wordmark">Lindeneck</p>
    <svg class="brand-dot" viewBox="0 0 140 140" aria-hidden="true">
      <circle cx="70" cy="70" r="66" fill="var(--sky)" stroke="var(--brown)" stroke-width="4"/>
    </svg>
    <div class="web">www.lindeneck-ferienhaus.de</div>
    <div class="contact-band">
      <div class="contact-line contact-line--address">
        <svg class="icon" viewBox="0 0 12 12" aria-hidden="true"><path d="M6 0a4 4 0 0 0-4 4c0 3 4 8 4 8s4-5 4-8a4 4 0 0 0-4-4zm0 5.6A1.6 1.6 0 1 1 6 2.4a1.6 1.6 0 0 1 0 3.2z"/></svg>
        <span>Lindenweg 12, 91738 Erlhausen</span>
      </div>
      <div class="contact-line contact-line--reach">
        <svg class="icon" viewBox="0 0 12 12" aria-hidden="true"><path d="M0 2h12v1L6 7 0 3z M0 4.2l6 4 6-4V10H0z"/></svg>
        <span>info@lindeneck-ferienhaus.de</span>
        <span class="gap"></span>
        <svg class="icon" viewBox="0 0 12 12" aria-hidden="true"><path d="M2.5 0.5l2 2.2-1 1.3c.6 1.6 2 3 3.5 3.6l1.3-1 2.2 2-1 2C5.5 10.6 1.2 6.3.6 1.5z"/></svg>
        <span>09841/5562170</span>
      </div>
    </div>
  </section>

  <section class="card card--back" aria-label="Visitenkarte Rückseite">
    <svg class="flap" viewBox="0 0 640 360" aria-hidden="true">
      <polygon points="0,0 640,0 320,250" fill="var(--sky)"/>
    </svg>
    <svg class="seal" viewBox="0 0 256 256" aria-hidden="true">
      <circle cx="128" cy="128" r="127" fill="var(--paper)"/>
      <circle cx="128" cy="128" r="116" fill="none" stroke="var(--brown)" stroke-width="4"/>
    </svg>
    <p class="seal-name">Lindeneck</p>
  </section>
</body>
</html>
```